" Somos uma clínica oftalmológica que atende nas principais cidades satélites do Distrito Federal. Já atuamos a 25 anos mas não possuímos um site de qualidade, possuímos um bem simples e, que na nossa opinião, é muito amador (http://nucleovisaoaurora.com.br/). Precisamos de um site que mostre o nosso comprometimento com o paciente, e nosso profissionalismo. Nos realizamos exames de vista, consultas e cirurgias oftalmológicas. Atendemos pacientes com convênio ou particular. A marcação de consultas é feita majoritariamente pelo telefone, mas queríamos uma forma de "pré-agendar" a consulta pelo site. Assim receberíamos a notificação por e-mail e entraríamos em contato com o cliente. "

```html
<!DOCTYPE html>
<html lang="pt-BR">
<head>
<meta charset="UTF-8">
<title>Núcleo Visão Aurora</title>
<link rel="stylesheet" href="https://fonts.googleapis.com/css2?family=Poppins:wght@400;500;600;700;800&display=swap">
<style>
  :root{
    --navy:#0b3f8f;
    --blue:#1565c8;
    --blue-soft:#2c7ad6;
    --white:#ffffff;
    --ink:#1f2d45;
    --muted:#6b7a90;
    --stage:#eef1f5;
    --hero-a:#9fb7d3;
    --hero-b:#3f6fa6;
    --hero-c:#12305f;
  }
  *{box-sizing:border-box;margin:0;padding:0}
  html,body{width:1200px;height:1200px;overflow:hidden;background:var(--stage);font-family:"Poppins",sans-serif}
  .site{position:absolute;left:0;top:235px;width:1200px;height:730px;background:var(--white);box-shadow:0 20px 50px rgba(20,40,80,.15);overflow:hidden}
  .topbar{height:30px;background:var(--navy);color:var(--white);display:flex;align-items:center;padding:0 170px;font-size:11px;gap:26px}
  .topbar .info{display:flex;align-items:center;gap:7px;opacity:.9;white-space:nowrap}
  .topbar .booking{margin-left:auto;display:flex;align-items:center;gap:7px;background:var(--blue-soft);height:30px;padding:0 16px;font-size:11px;white-space:nowrap}
  .topbar .booking b{font-weight:700}
  .navbar{height:80px;display:flex;align-items:center;padding:0 170px;border-bottom:1px solid #e5e9ef}
  .brand{display:flex;align-items:center;gap:9px;white-space:nowrap}
  .brand-dot{width:26px;height:26px;border-radius:50%;background:var(--blue)}
  .brand-name{font-weight:700;font-size:15px;color:var(--navy);letter-spacing:.2px}
  .menu{margin-left:auto;display:flex;gap:34px;list-style:none;font-size:11px;font-weight:600;color:var(--ink);white-space:nowrap}
  .menu li:first-child{color:var(--blue)}
  .socials{display:flex;gap:14px;margin-left:46px}
  .socials span{width:14px;height:14px;border-radius:50%;background:var(--blue)}
  .hero{position:relative;height:620px}
  .hero-photo{position:absolute;inset:0;background:linear-gradient(100deg,var(--hero-c) 0%,var(--hero-b) 45%,var(--hero-a) 100%)}
  .hero-shade{position:absolute;inset:0;background:linear-gradient(90deg,rgba(10,30,70,.55) 0%,rgba(10,30,70,.1) 60%,rgba(0,0,0,0) 100%)}
  .hero-copy{position:absolute;left:170px;top:185px;color:var(--white)}
  .headline{display:flex;align-items:flex-end;gap:12px;line-height:1}
  .headline .years{font-size:118px;font-weight:800;letter-spacing:-3px;line-height:.82}
  .headline .lines{font-weight:700;font-size:40px;line-height:1.08;text-transform:uppercase}
  .headline .lines small{display:block;font-size:24px;font-weight:600}
  .cta{display:inline-block;margin:40px 0 0 150px;border:1px solid rgba(255,255,255,.7);color:var(--white);font-size:11px;letter-spacing:1px;padding:9px 20px}
  .video{position:absolute;left:140px;bottom:80px;display:flex;align-items:center;gap:12px;color:var(--white);font-size:9px;line-height:1.3;font-weight:500}
  .dots{position:absolute;left:50%;bottom:60px;transform:translateX(-50%);display:flex;gap:7px}
  .dots span{width:9px;height:9px;border-radius:50%;background:rgba(255,255,255,.75)}
  .dots span:first-child{background:transparent;border:2px solid var(--white)}
</style>
</head>
<body>
<main class="site">
  <div class="topbar">
    <span class="info">
      <svg width="11" height="11" viewBox="0 0 24 24" fill="#fff"><path d="M6.6 10.8a15 15 0 0 0 6.6 6.6l2.2-2.2c.3-.3.7-.4 1-.2 1.1.4 2.3.6 3.6.6.6 0 1 .4 1 1V20c0 .6-.4 1-1 1A17 17 0 0 1 3 4c0-.6.4-1 1-1h3.5c.6 0 1 .4 1 1 0 1.3.2 2.5.6 3.6.1.3 0 .7-.2 1z"/></svg>
      (61) 3210-4580
    </span>
    <span class="info">
      <svg width="10" height="12" viewBox="0 0 24 28" fill="#fff"><path d="M12 0a9 9 0 0 0-9 9c0 7 9 19 9 19s9-12 9-19a9 9 0 0 0-9-9zm0 13a4 4 0 1 1 0-8 4 4 0 0 1 0 8z"/></svg>
      Av. Central, 25 - Taguatinga / DF
    </span>
    <span class="booking">
      <svg width="12" height="12" viewBox="0 0 24 24" fill="#fff"><path d="M6.6 10.8a15 15 0 0 0 6.6 6.6l2.2-2.2c.3-.3.7-.4 1-.2 1.1.4 2.3.6 3.6.6.6 0 1 .4 1 1V20c0 .6-.4 1-1 1A17 17 0 0 1 3 4c0-.6.4-1 1-1h3.5c.6 0 1 .4 1 1 0 1.3.2 2.5.6 3.6.1.3 0 .7-.2 1z"/></svg>
      Marcar Consulta <b>FalaVisão</b>
    </span>
  </div>

  <nav class="navbar">
    <div class="brand">
      <span class="brand-dot"></span>
      <span class="brand-name">NÚCLEO VISÃO AURORA</span>
    </div>
    <ul class="menu">
      <li>HOME</li>
      <li>QUEM SOMOS</li>
      <li>SERVIÇOS</li>
      <li>BLOG</li>
      <li>CONTATO</li>
    </ul>
    <div class="socials"><span></span><span></span><span></span><span></span><span></span></div>
  </nav>

  <section class="hero">
    <div class="hero-photo" role="img" aria-label="Fotografia de um exame oftalmológico: médico com luvas examinando o olho de uma paciente"></div>
    <div class="hero-shade"></div>
    <div class="hero-copy">
      <div class="headline">
        <span class="years">25</span>
        <span class="lines"><small>ANOS</small>De história e<br>profissionalismo</span>
      </div>
      <span class="cta">MARCAR CONSULTA</span>
    </div>
    <div class="video">
      <svg width="26" height="26" viewBox="0 0 26 26"><circle cx="13" cy="13" r="12" fill="none" stroke="#fff" stroke-width="1.5"/><path d="M10.5 8.5v9l7-4.5z" fill="#fff"/></svg>
      <span>VER O<br>VÍDEO AGORA</span>
    </div>
    <div class="dots"><span></span><span></span><span></span><span></span><span></span></div>
  </section>
</main>
</body>
</html>
```